Kelvard Engineers: Why you should hire us keepsake

New design. Open to plastic cards. We are an engineering firm that designs cell phone towers and commercial buildings. Please check out our website www.kelvardeng.example for more details. We want people to remember our card and for it to be useful if possible. We want the same look and feel on these cards to be translated to other marketing material we may need such as brochures.

Target Market(s)

Architects, Developers and Telecommunication Carriers

Industry/Entity Type

Engineering

Contact Information for Business Card

Card with our company colors, logo, and innovative design with elements related to our industry.

Font styles to use
Sans Serif

Colors
9bcb3c
abd036
0255a3

Requirements
Must have
• Sleek and hip design
Nice to have
• Bright lime green and navy coloring that pops with an innovative design.
Should not have
• A basic and boring design

```html
<!DOCTYPE html>
<html lang="en">
<head>
<meta charset="utf-8">
<title>Kelvard Engineers Business Card</title>
<link href="https://fonts.googleapis.com/css2?family=Archivo:wght@400;500;700;900&display=swap" rel="stylesheet">
<style>
  :root {
    --navy: #0c2b68;
    --navy-deep: #0a2359;
    --lime: #2fe02f;
    --cream: #efeee4;
    --grey-text: #c9cfdc;
    --ink: #1b2a5a;
    --stage: #e4e5e8;
  }
  * { margin: 0; padding: 0; box-sizing: border-box; }
  html, body { width: 1200px; height: 786px; overflow: hidden; }
  body {
    background: var(--stage);
    font-family: "Archivo", Arial, sans-serif;
    display: flex;
    align-items: center;
    justify-content: center;
    gap: 40px;
  }
  .card {
    position: relative;
    width: 520px;
    height: 297px;
    border-radius: 16px;
    overflow: hidden;
    box-shadow: 0 10px 30px rgba(10, 25, 60, 0.25);
  }

  /* Front */
  .card-front { background: var(--navy); }
  .front-brand {
    position: absolute;
    left: 150px;
    top: 74px;
    font-weight: 900;
    font-size: 64px;
    letter-spacing: -1px;
    color: var(--lime);
    line-height: 1;
  }
  .front-tagline {
    position: absolute;
    left: 152px;
    top: 148px;
    font-size: 15px;
    font-weight: 500;
    color: var(--lime);
    text-transform: uppercase;
    letter-spacing: 0.5px;
  }
  .front-cities {
    position: absolute;
    left: 0;
    right: 0;
    bottom: 34px;
    text-align: center;
    font-size: 12px;
    letter-spacing: 4px;
    color: var(--grey-text);
    text-transform: uppercase;
  }
  .front-cities .sep { color: var(--lime); margin: 0 8px; }

  /* Back */
  .card-back { background: var(--cream); }
  .back-swoosh { position: absolute; inset: 0; }
  .back-brand {
    position: absolute;
    left: 40px;
    top: 42px;
    font-weight: 900;
    font-size: 44px;
    letter-spacing: -1px;
    color: var(--lime);
    line-height: 1;
  }
  .contact {
    position: absolute;
    left: 250px;
    top: 100px;
    padding-left: 18px;
    border-left: 1px solid rgba(27, 42, 90, 0.25);
    color: var(--ink);
  }
  .contact-name {
    font-weight: 700;
    font-size: 16px;
    text-transform: uppercase;
    color: var(--navy);
    margin-bottom: 12px;
    letter-spacing: 0.3px;
  }
  .contact-line {
    display: flex;
    align-items: center;
    gap: 7px;
    font-size: 12px;
    line-height: 18px;
  }
  .contact-line svg { width: 11px; height: 11px; flex: none; }
  .contact-address {
    font-size: 12px;
    line-height: 17px;
    margin-top: 8px;
  }
</style>
</head>
<body>

  <section class="card card-front" aria-label="Card front">
    <div class="front-brand">Kelvard</div>
    <div class="front-tagline">Multi-Discipline Engineering</div>
    <div class="front-cities">
      Atlanta<span class="sep">/</span>Charlotte<span class="sep">/</span>Houston<span class="sep">/</span>San Antonio
    </div>
  </section>

  <section class="card card-back" aria-label="Card back">
    <svg class="back-swoosh" viewBox="0 0 520 297" preserveAspectRatio="none" aria-hidden="true">
      <path d="M0 60 C 70 110, 150 150, 200 297 L0 297 Z" fill="var(--navy)"/>
      <path d="M0 48 C 80 100, 160 150, 212 297 L200 297 C 150 150, 70 110, 0 60 Z" fill="var(--lime)"/>
      <path d="M0 40 C 90 95, 168 150, 222 297 L212 297 C 160 150, 80 100, 0 48 Z" fill="#ffffff" opacity="0.8"/>
    </svg>

    <div class="back-brand">Kelvard</div>

    <div class="contact">
      <div class="contact-name">Dana Whitfield Moore</div>
      <div class="contact-line">
        <svg viewBox="0 0 12 12"><rect x="3" y="1" width="6" height="10" rx="1" fill="none" stroke="var(--lime)" stroke-width="1.4"/></svg>
        555.014.2231
      </div>
      <div class="contact-line">
        <svg viewBox="0 0 12 12"><path d="M2 1.5 L4.5 1.5 L5.5 4 L4 5 C4.8 6.8 5.6 7.6 7 8.2 L8 6.7 L10.5 7.7 L10.5 10.2 C6 10.5 1.5 6 2 1.5 Z" fill="var(--lime)"/></svg>
        555.014.7718
      </div>
      <div class="contact-line">
        <svg viewBox="0 0 12 12"><rect x="1" y="2.5" width="10" height="7" fill="var(--lime)"/><path d="M1 2.5 L6 6.5 L11 2.5" fill="none" stroke="var(--cream)" stroke-width="1"/></svg>
        dmoore@kelvardeng.example
      </div>
      <div class="contact-address">
        2400 Larkspur Commons Pkwy<br>
        Suite 310 Brantley, GA 30999
      </div>
    </div>
  </section>

</body>
</html>
```